Menu Design Project

My Restaurant is called The Pita Corner, it's fast food restaurant serves Gyro, Wings, Subs, Fried Seafood and chicken tenders. I'm looking for a menu design to fit the fast food category and have some photos of the food on the front page as well inside the menu. I will attached some photos and you can add any other photo related to the menu from the web.

Industry/Entity Type

Restaurant

```html
<!DOCTYPE html>
<html lang="en">
<head>
<meta charset="UTF-8">
<title>The Pita Corner – Menu</title>
<link href="https://fonts.googleapis.com/css2?family=Arimo:wght@400;700&family=Questrial&family=Montserrat:wght@600;700&family=Oswald:wght@300;500&family=Great+Vibes&display=swap" rel="stylesheet">
<style>
  :root {
    --red: #e3141b;
    --red-deep: #b80b10;
    --red-soft: #f27a7d;
    --black: #111;
    --white: #fff;
    --ink: #222;
    --canvas: #e6e6e8;
  }
  * { box-sizing: border-box; margin: 0; padding: 0; }
  html, body { width: 1200px; height: 770px; overflow: hidden; }
  body { background: var(--canvas); font-family: "Questrial", sans-serif; color: var(--ink); position: relative; }

  .sheet { position: absolute; top: 25px; width: 570px; height: 720px; box-shadow: 0 4px 14px rgba(0,0,0,.25); }
  .sheet--outside { left: 15px; }
  .sheet--inside { left: 615px; }
  .half { position: absolute; left: 0; width: 570px; height: 360px; overflow: hidden; }
  .half--top { top: 0; }
  .half--bottom { top: 360px; }

  /* ---------- outside ---------- */
  .cover { background: radial-gradient(ellipse at 50% 45%, #f12a2f 0%, var(--red) 45%, var(--red-deep) 100%); color: var(--white); }
  .back { transform: rotate(180deg); }
  .checker-corner { position: absolute; width: 120px; height: 70px; background: linear-gradient(135deg, #f6b9bb, var(--red-soft)); }
  .checker-corner--tr { right: 0; top: 0; clip-path: polygon(0 0, 100% 0, 100% 100%); }
  .checker-corner--bl { left: 0; bottom: 0; clip-path: polygon(0 0, 0 100%, 100% 100%); }
  .checker-corner--tl { left: 0; top: 0; width: 70px; height: 50px; clip-path: polygon(0 0, 100% 0, 0 100%); }
  .checker-corner--tr-sm { right: 0; top: 0; width: 90px; height: 50px; clip-path: polygon(0 0, 100% 0, 100% 100%); }

  .brand-mark { position: absolute; left: 50%; top: 24px; transform: translateX(-50%); display: flex; align-items: center; gap: 6px; }
  .brand-mark .dot { width: 34px; height: 34px; border-radius: 50%; background: var(--white); }
  .brand-name { position: absolute; top: 70px; left: 0; right: 0; text-align: center; font: 700 15px "Arimo", sans-serif; color: var(--black); }
  .cutlery { position: absolute; top: 95px; width: 80px; height: 80px; border-radius: 12px; background: linear-gradient(135deg, #e8e4dc, #c9b48a); }
  .cutlery--left { left: 38px; }
  .cutlery--right { right: 38px; }
  .menu-word { position: absolute; top: 100px; left: 0; right: 0; text-align: center; font: 58px "Great Vibes", cursive; }
  .menu-rule { position: absolute; top: 172px; left: 50%; width: 130px; margin-left: -65px; height: 1px; background: var(--white); }
  .food-photo { position: absolute; border-radius: 8px; }
  .food-photo--wings { left: 95px; top: 200px; width: 95px; height: 65px; background: radial-gradient(circle, #c4541d, #7d2a0d); }
  .food-photo--burger { left: 230px; top: 196px; width: 100px; height: 70px; background: linear-gradient(#d89a48, #6b3a1a 55%, #caa35a); }
  .food-photo--gyro { left: 375px; top: 194px; width: 110px; height: 72px; background: radial-gradient(circle, #c99c6a, #6f4a2b); }
  .hours { position: absolute; top: 283px; left: 0; right: 0; text-align: center; font: 300 16px "Oswald", sans-serif; }
  .hours strong { font-weight: 500; }
  .contact-bar { position: absolute; left: 12px; right: 12px; bottom: 14px; height: 28px; background: var(--black); color: var(--white); display: flex; align-items: center; justify-content: center; gap: 14px; font: 14px "Questrial", sans-serif; }
  .contact-bar svg { width: 12px; height: 12px; }

  .slogan-bar { position: absolute; left: 12px; right: 12px; top: 14px; height: 30px; background: var(--black); color: var(--white); font: 22px "Great Vibes", cursive; display: flex; align-items: center; padding-left: 30px; }
  .drinks { position: absolute; left: 330px; top: 58px; width: 170px; }
  .drinks-list { font-size: 11px; line-height: 15px; margin-top: 6px; padding-left: 14px; }
  .drink-cans { position: absolute; left: 255px; top: 60px; width: 70px; height: 75px; border-radius: 6px; background: linear-gradient(90deg, #c01a1a, #2e8b3a, #f08a16, #c01a1a); }
  .map { position: absolute; left: 40px; top: 55px; width: 200px; height: 140px; border-radius: 16px; border: 3px solid #bdbdbd; background: linear-gradient(135deg, #f1f1ef, #d6d6d2); }
  .pickup { position: absolute; left: 290px; top: 200px; width: 230px; font-size: 11px; }
  .pickup .phone { font: 700 14px "Arimo", sans-serif; margin-top: 2px; }
  .pickup-icon { position: absolute; left: 232px; top: 192px; width: 30px; height: 30px; border-radius: 50%; background: var(--black); }
  .back-hours { position: absolute; left: 40px; top: 210px; font-size: 12px; }
  .back-hours strong { display: block; font: 700 14px "Arimo", sans-serif; }
  .back-address { position: absolute; left: 60px; right: 40px; top: 258px; font-size: 11px; display: flex; justify-content: space-between; }

  /* ---------- inside ---------- */
  .frame { background: var(--red); padding: 10px; }
  .page { position: relative; width: 100%; height: 100%; background: var(--white); overflow: hidden; }
  .page-title { position: absolute; top: 16px; left: 0; right: 0; display: flex; flex-direction: column; align-items: center; gap: 4px; font: 700 13px "Arimo", sans-serif; color: var(--black); }
  .page-title .dot { width: 22px; height: 22px; border-radius: 50%; border: 3px solid var(--red); }
  .tab { position: absolute; height: 18px; background: var(--black); color: var(--white); font: 700 11px "Montserrat", sans-serif; text-transform: uppercase; letter-spacing: 1px; display: flex; align-items: center; gap: 8px; padding: 0 10px; white-space: nowrap; }
  .tab::before { content: ""; flex: none; width: 8px; height: 8px; border-radius: 50%; background: var(--white); box-shadow: inset 0 0 0 2px var(--red); }
  .tab small { font-size: 8px; letter-spacing: .5px; }
  .price-list { position: absolute; list-style: none; font-size: 10.5px; }
  .price-list li { display: flex; justify-content: space-between; gap: 8px; height: 15.5px; align-items: center; white-space: nowrap; }
  .price-list .note { color: var(--red); justify-content: flex-start; }
  .price-list .price { color: var(--black); }
  .price-list--kids { font-size: 10px; }
  .price-list--kids li { height: 17px; }
  .price-list--kids .price { color: var(--red); font-weight: 700; }
  .price-list .extra { color: var(--red); font-size: 7px; margin-left: 4px; }
  .inside-photo { position: absolute; border-radius: 6px; }
  .inside-photo--nuggets { left: 8px; bottom: 10px; width: 140px; height: 100px; background: radial-gradient(circle at 40% 60%, #e0a44a, #b5141a 75%); }
  .inside-photo--fries { right: 10px; bottom: 12px; width: 115px; height: 85px; background: radial-gradient(circle at 40% 50%, #f3c64b, #c8891f 60%, #b5141a); }
</style>
</head>
<body>

  <!-- Outside: back cover (printed inverted for folding) and front cover -->
  <section class="sheet sheet--outside">
    <div class="half half--top cover back">
      <div class="slogan-bar">Good Food, Good Mood</div>
      <div class="map" role="img" aria-label="Street map showing the restaurant location"></div>
      <div class="drink-cans" role="img" aria-label="Photo of assorted soda cans"></div>
      <div class="drinks">
        <div class="tab" style="position:relative;width:110px">Drinks</div>
        <p class="drinks-list">Cola, Diet Cola,<br>Lemon-Lime, Sport Drink,<br>Strawberry Soda,<br>Orange Soda,<br>Pepper Soda and more.</p>
      </div>
      <div class="pickup-icon" role="img" aria-label="Bowl and serving illustration"></div>
      <div class="pickup">
        <p>Call Us for Pick Up orders or Catering</p>
        <p class="phone">713-555-0186</p>
      </div>
      <div class="back-hours">Hours of operation:<strong>Monday to Sunday 11am-9pm</strong></div>
      <div class="back-address"><span>4120 Cedar Hollow Ave, Houston, TX 77021</span><span>713-555-0186</span></div>
      <div class="checker-corner checker-corner--bl" role="img" aria-label="Red and white checkered corner"></div>
    </div>

    <div class="half half--bottom cover front">
      <div class="checker-corner checker-corner--tr" role="img" aria-label="Red and white checkered corner"></div>
      <div class="brand-mark"><span class="dot"></span></div>
      <h1 class="brand-name">The Pita Corner Restaurant</h1>
      <div class="cutlery cutlery--left" role="img" aria-label="Fork and spoon tied with a gold bow"></div>
      <div class="cutlery cutlery--right" role="img" aria-label="Fork and spoon tied with a gold bow"></div>
      <div class="menu-word">Menu</div>
      <div class="menu-rule"></div>
      <div class="food-photo food-photo--wings" role="img" aria-label="Photo of fried chicken wings"></div>
      <div class="food-photo food-photo--burger" role="img" aria-label="Photo of a burger"></div>
      <div class="food-photo food-photo--gyro" role="img" aria-label="Photo of a gyro wrap"></div>
      <p class="hours">Hours of operation: <strong>Monday to Sunday 11am-9pm</strong></p>
      <div class="contact-bar">
        <svg viewBox="0 0 12 12"><path d="M6 0a4 4 0 0 1 4 4c0 3-4 8-4 8S2 7 2 4a4 4 0 0 1 4-4z" fill="#fff"/><circle cx="6" cy="4" r="1.5" fill="#111"/></svg>
        <span>4120 Cedar Hollow Ave, Houston, TX 77021</span>
        <svg viewBox="0 0 12 12"><circle cx="6" cy="6" r="5.3" fill="none" stroke="#fff"/><path d="M4 3.2l1 1-.6.8c.4.9 1 1.5 1.8 1.8l.8-.6 1 1-.9.9C5 7.8 4.2 7 3.2 5z" fill="#fff"/></svg>
        <span>713-555-0186</span>
      </div>
    </div>
  </section>

  <!-- Inside spread -->
  <section class="sheet sheet--inside">
    <div class="half half--top frame">
      <div class="page">
        <div class="checker-corner checker-corner--tl" role="img" aria-label="Red and white checkered corner"></div>
        <div class="checker-corner checker-corner--tr-sm" role="img" aria-label="Red and white checkered corner"></div>
        <div class="page-title"><span class="dot"></span>The Pita Corner Menu</div>

        <div class="tab" style="left:0;top:60px;width:110px">Chicken</div>
        <ul class="price-list" style="left:22px;top:82px;width:200px">
          <li>10 Large Wings<span class="price">$8.99</span></li>
          <li>20 Large Wings<span class="price">$16.99</span></li>
          <li>30 Large Wings<span class="price">$23.99</span></li>
          <li>50 Large Wings<span class="price">$39.99</span></li>
          <li>½ lb. Chicken Strips<span class="price">$5.49</span></li>
          <li>1lb. Chicken Strips<span class="price">$7.99</span></li>
          <li>½ lb. Gizzards<span class="price">$5.49</span></li>
          <li>1lb. Gizzards<span class="price">$7.99</span></li>
        </ul>

        <div class="tab" style="left:10px;top:214px;width:110px">Seafood</div>
        <ul class="price-list" style="left:32px;top:236px;width:200px">
          <li>½ lb. Shrimp<span class="price">$7.99</span></li>
          <li>1lb. Shrimp<span class="price">$13.99</span></li>
          <li>½ lb. Fish<span class="price">$6.99</span></li>
          <li>1lb. Fish<span class="price">$12.99</span></li>
        </ul>

        <div class="tab" style="right:0;top:60px;width:150px">Fresh Salad</div>
        <ul class="price-list" style="left:255px;top:82px;width:265px">
          <li>Caesar Salad<span class="price">$4.95</span></li>
          <li>Gyro Salad<span class="price">$5.95</span></li>
          <li>Shrimp Caesar Salad<span class="price">$6.25</span></li>
          <li>Greek Salad<span class="price">$5.95</span></li>
        </ul>

        <div class="tab" style="right:0;top:152px;width:150px">Gyro &amp; Subs</div>
        <ul class="price-list" style="left:260px;top:174px;width:265px">
          <li>Gyro (Original or Chicken)<span class="price">$6.99</span></li>
          <li>¼ lb. Black Angus Burger<span class="price">$3.99</span></li>
          <li>Buffalo Chicken Sandwich<span class="price">$5.99</span></li>
          <li class="note">YOUR CHOICE OF 6" OR FOOTLONG SUBS</li>
          <li>Po Boy Shrimp<span class="price">$7.55-$9.25</span></li>
          <li>Philly (Steak or Chicken)<span class="price">$6.75-$8.99</span></li>
          <li>Fish<span class="price">$6.75-$8.99</span></li>
          <li>Turkey &amp; Cheese<span class="price">$6.49-$7.95</span></li>
        </ul>
      </div>
    </div>

    <div class="half half--bottom frame">
      <div class="page">
        <div class="tab" style="left:0;top:12px;width:100px">Sides</div>
        <ul class="price-list" style="left:15px;top:34px;width:200px">
          <li>French Fries<span class="price">$2.79</span></li>
          <li>Cajun Fries<span class="price">$3.99</span></li>
          <li>Onion Rings<span class="price">$4.99</span></li>
          <li>5 Jalapeño Poppers<span class="price">$4.99</span></li>
          <li>Fried Okra<span class="price">$4.99</span></li>
          <li>Fried Mushroom<span class="price">$5.49</span></li>
          <li>5 Mozzarella Sticks<span class="price">$5.49</span></li>
        </ul>

        <div class="tab" style="right:0;top:30px;width:290px">Combos <small>includes 16oz soft drink!</small></div>
        <ul class="price-list" style="left:245px;top:54px;width:285px">
          <li>½ lb. Fish &amp; Fries<span class="price">$9.99</span></li>
          <li>½ lb. Shrimp &amp; Fries<span class="price">$10.99</span></li>
          <li>6" Philly (Steak or Chicken) &amp; Fries<span class="price">$9.99</span></li>
          <li>Gyro (Original, Chicken or Fish) &amp; Fries<span class="price">$9.49</span></li>
          <li>5 Wings &amp; Fries<span class="price">$9.49</span></li>
          <li>½ lb. Gizzards &amp; Fries<span class="price">$7.99</span></li>
          <li>¼ lb. Black Angus Burger &amp; Fries<span class="price">$6.99<span class="extra">*CHEESE EXTRA</span></span></li>
          <li>5 Wings &amp; Gizzards<span class="price">$11.49</span></li>
          <li>½ lb. Chicken Strips &amp; Fries<span class="price">$7.99</span></li>
        </ul>

        <div class="tab" style="left:215px;top:206px;width:130px">Kids Meal</div>
        <ul class="price-list price-list--kids" style="left:158px;top:232px;width:262px">
          <li>Chicken Nuggets 4pc with small drink and fries<span class="price">$4.95</span></li>
          <li>Chicken Strips 2pc with small drink and fries<span class="price">$4.95</span></li>
          <li>Mac &amp; Cheese<span class="price">$3.95</span></li>
        </ul>

        <div class="inside-photo inside-photo--nuggets" role="img" aria-label="Photo of chicken nuggets, burger, fries and a soft drink"></div>
        <div class="inside-photo inside-photo--fries" role="img" aria-label="Photo of chicken strips, fries and a soft drink"></div>
      </div>
    </div>
  </section>

</body>
</html>
```